Flyer for my live dj set from a recent party (party flyer included)

Need a recreation of a flyer for my live dj mix from the night of the party

(I added a pic of me and my logo if that looks good as well):

TEXT:

NO SLEEPING UNDER THE MIRROR BALL

VELTRA PRODUCTIONS One Year Anniversary Party 2019

MORVIN (Closing Set)

Recorded Live at Redgate Hollow Brewery

linkspace.net/morvin482

Target Market(s)

Electronic Music, Nightclub goers

Industry/Entity Type

Night Club

Font styles to use
Sans Serif

Colors

Designer to choose colors to be used in the design.

Requirements
Must have
• Elements of the original party flyer
Nice to have
• Some bright or neon, something that pops. Try to keep it similar to the flyer attached so it has the same theme and looks like a promo mix for that party

```html
<!DOCTYPE html>
<html lang="en">
<head>
<meta charset="UTF-8">
<title>Veltra Productions – Morvin Live Mix</title>
<link rel="stylesheet" href="https://fonts.googleapis.com/css2?family=Teko:wght@500&family=Oswald:wght@500&family=Audiowide&family=Black+Ops+One&family=Russo+One&family=Montserrat:wght@400&display=swap">
<style>
  :root {
    --page-bg: #e6ecee;
    --poster-top: #07071a;
    --poster-bottom: #222226;
    --gold: #f5c400;
    --gold-light: #f3d36a;
    --gold-dark: #c9971f;
    --cyan: #5fe0ea;
    --cyan-glow: rgba(60, 220, 240, 0.75);
    --navy-ink: #17183a;
    --white: #ffffff;
    --band-dark: #2a2a34;
  }
  * { margin: 0; padding: 0; box-sizing: border-box; }
  html, body {
    width: 1200px; height: 1200px; overflow: hidden;
    background: var(--page-bg);
  }
  .poster {
    position: absolute; left: 177px; top: 20px;
    width: 846px; height: 1160px; overflow: hidden;
    background: linear-gradient(180deg, var(--poster-top) 0%, #0c0c22 60%, var(--poster-bottom) 88%);
  }
  .photo-area {
    position: absolute; left: 0; top: 150px; width: 846px; height: 900px;
    background:
      radial-gradient(ellipse 50% 42% at 50% 48%, rgba(150, 120, 230, 0.85) 0%, rgba(70, 60, 200, 0.7) 40%, rgba(30, 30, 110, 0.45) 70%, transparent 100%),
      radial-gradient(ellipse 60% 18% at 60% 92%, rgba(200, 40, 90, 0.45) 0%, transparent 100%);
  }
  .poster-header {
    position: absolute; top: 44px; left: 0; width: 100%; text-align: center;
  }
  .producer {
    font-family: "Teko", sans-serif; font-weight: 500;
    font-size: 40px; letter-spacing: 9px; color: var(--white); line-height: 1;
  }
  .event-title {
    font-family: "Oswald", sans-serif; font-weight: 500;
    font-size: 62px; color: var(--gold); line-height: 1; margin-top: 18px;
    transform: scaleX(0.86); letter-spacing: 0.5px;
  }
  .event-year {
    font-family: "Audiowide", sans-serif; font-size: 96px; line-height: 1;
    color: var(--cyan); margin-top: 10px; font-style: italic;
    text-shadow: 0 0 14px var(--cyan-glow), 0 0 30px var(--cyan-glow);
  }
  .poster-art { position: absolute; left: 0; top: 0; width: 846px; height: 1160px; }
  .artist-name { font-family: "Black Ops One", sans-serif; fill: var(--white); }
  .band-text { font-family: "Russo One", sans-serif; }
  .band-text--dark { fill: var(--navy-ink); }
  .band-text--light { fill: var(--white); }
  .poster-footer {
    position: absolute; top: 1035px; left: 0; width: 100%; text-align: center;
    font-family: "Montserrat", sans-serif; font-weight: 400; color: var(--white);
  }
  .venue { font-size: 27px; letter-spacing: 0.5px; }
  .weblink { font-size: 28px; margin-top: 6px; display: inline-flex; align-items: center; gap: 8px; }
  .weblink-mark { width: 20px; height: 20px; background: var(--gold); border-radius: 3px; }
</style>
</head>
<body>
  <main class="poster">
    <div class="photo-area" role="img" aria-label="Photo of the DJ performing at the turntables against a blue-lit brick wall"></div>

    <header class="poster-header">
      <p class="producer">VELTRA PRODUCTIONS</p>
      <h1 class="event-title">ONE YEAR ANNIVERSARY PARTY</h1>
      <p class="event-year">2019</p>
    </header>

    <svg class="poster-art" viewBox="0 0 705 966" aria-hidden="false">
      <defs>
        <linearGradient id="goldBand" x1="0" y1="0" x2="1" y2="0">
          <stop offset="0" stop-color="var(--gold-dark)"/>
          <stop offset="0.5" stop-color="var(--gold-light)"/>
          <stop offset="1" stop-color="var(--gold)"/>
        </linearGradient>
        <linearGradient id="darkBand" x1="0" y1="0" x2="0" y2="1">
          <stop offset="0" stop-color="#3a3a46"/>
          <stop offset="1" stop-color="#18181e"/>
        </linearGradient>
      </defs>

      <text class="artist-name" x="300" y="644" font-size="64" text-anchor="middle" transform="rotate(-4 300 623)">MORVIN</text>

      <polygon class="band band--gold" points="65,703 578,631 555,705 28,786" fill="url(#goldBand)"/>
      <text class="band-text band-text--dark" x="300" y="722" font-size="36" text-anchor="middle"
            textLength="440" lengthAdjust="spacingAndGlyphs" transform="rotate(-8.3 300 708)">NO SLEEPING UNDER</text>

      <polygon class="band band--dark" points="148,758 660,693 637,768 113,838" fill="url(#darkBand)" stroke="#cfd0d8" stroke-width="1.5"/>
      <text class="band-text band-text--light" x="388" y="782" font-size="36" text-anchor="middle"
            textLength="430" lengthAdjust="spacingAndGlyphs" transform="rotate(-7.5 388 768)">THE MIRROR BALL</text>
    </svg>

    <footer class="poster-footer">
      <p class="venue">RECORDED LIVE AT REDGATE HOLLOW BREWERY</p>
      <p class="weblink"><span class="weblink-mark"></span>linkspace.net/morvin482</p>
    </footer>
  </main>
</body>
</html>
```